Business Card Design Project - Photographer

Photography business needs a logo. I would like to see creative licence on options on 1 & 2 sided. I really like the concept of a fully / partially frosted design. I have already used ArtHive for my Logo, so I am looking for the same level of assistance with this project.

If you have any questions please let me know

Cheers Morris

Industry/Entity Type

Business

Requirements
Must have
• These are my contact details
Name: Morris Tilbury
Mobile: 0438 216 907
email: morris@brightlensstudio.com.au
Website: www.brightlensstudio.com.au
Nice to have
• Facebook: https://www.facebook.com/BrightLensStudioAus

```html
<!DOCTYPE html>
<html lang="en">
<head>
<meta charset="utf-8">
<title>Bright Lens Studio – Business Card</title>
<link href="https://fonts.googleapis.com/css2?family=Mulish:wght@400;700&display=swap" rel="stylesheet">
<style>
  :root {
    --backdrop: #3a3a3a;
    --card: #ffffff;
    --accent: #d3242a;
    --ink: #1e1e1e;
    --rule: #222222;
  }
  * { box-sizing: border-box; margin: 0; padding: 0; }
  html, body {
    width: 1200px;
    height: 736px;
    overflow: hidden;
    background: var(--backdrop);
    font-family: "Mulish", sans-serif;
  }
  .business-card {
    position: absolute;
    left: 150px;
    top: 111px;
    width: 900px;
    height: 514px;
    background: var(--card);
    box-shadow: 0 18px 40px rgba(0,0,0,0.45);
  }
  .edge-band {
    position: absolute;
    width: 16px;
    background: var(--accent);
  }
  .edge-band--left { left: 0; top: 60px; height: 250px; }
  .edge-band--right { right: 0; top: 220px; height: 240px; }

  .brand {
    position: absolute;
    left: 110px;
    top: 198px;
    display: flex;
    align-items: center;
    gap: 14px;
  }
  .brand-mark {
    width: 40px;
    height: 40px;
    background: var(--accent);
  }
  .brand-name {
    font-weight: 700;
    font-size: 27px;
    line-height: 1.1;
    color: var(--accent);
  }
  .divider {
    position: absolute;
    left: 370px;
    top: 190px;
    width: 2px;
    height: 80px;
    background: var(--rule);
  }
  .contact {
    position: absolute;
    left: 390px;
    top: 160px;
    color: var(--ink);
  }
  .contact-name {
    font-weight: 700;
    font-size: 24px;
    margin-left: 48px;
    margin-bottom: 4px;
  }
  .contact-list { list-style: none; }
  .contact-item {
    display: flex;
    align-items: center;
    gap: 12px;
    font-size: 25px;
    line-height: 37px;
  }
  .contact-icon {
    width: 18px;
    height: 18px;
    flex: none;
  }
</style>
</head>
<body>
  <main class="business-card">
    <div class="edge-band edge-band--left"></div>
    <div class="edge-band edge-band--right"></div>

    <div class="brand">
      <span class="brand-mark"></span>
      <span class="brand-name">Bright Lens<br>Studio</span>
    </div>

    <div class="divider"></div>

    <section class="contact">
      <p class="contact-name">Morris Tilbury</p>
      <ul class="contact-list">
        <li class="contact-item">
          <svg class="contact-icon" viewBox="0 0 18 18"><circle cx="9" cy="9" r="8" fill="none" stroke="#d3242a" stroke-width="1.5"/><path d="M6 5.5l1.6-.5 1 2-1 .8a5 5 0 0 0 2.4 2.4l.8-1 2 1-.5 1.6c-3.5 0-6.3-2.8-6.3-6.3z" fill="#d3242a"/></svg>
          <span>0438 216 907</span>
        </li>
        <li class="contact-item">
          <svg class="contact-icon" viewBox="0 0 18 18"><circle cx="9" cy="9" r="8" fill="none" stroke="#d3242a" stroke-width="1.5"/><rect x="5" y="6" width="8" height="6" fill="none" stroke="#d3242a" stroke-width="1.2"/><path d="M5 6l4 3.2L13 6" fill="none" stroke="#d3242a" stroke-width="1.2"/></svg>
          <span>morris@brightlensstudio.com.au</span>
        </li>
        <li class="contact-item">
          <svg class="contact-icon" viewBox="0 0 18 18"><circle cx="9" cy="9" r="8" fill="none" stroke="#d3242a" stroke-width="1.5"/><circle cx="9" cy="9" r="4" fill="none" stroke="#d3242a" stroke-width="1.2"/><path d="M5 9h8M9 5v8" stroke="#d3242a" stroke-width="1"/></svg>
          <span>www.brightlensstudio.com.au</span>
        </li>
        <li class="contact-item">
          <svg class="contact-icon" viewBox="0 0 18 18"><circle cx="9" cy="9" r="8" fill="none" stroke="#d3242a" stroke-width="1.5"/></svg>
          <span>BrightLensStudioAus</span>
        </li>
      </ul>
    </section>
  </main>
</body>
</html>
```